Nexor Turbo Business Card Design

This is a start up company that has state of the art patented technology for turbo chargers,that can be used on engines, gas or diesel, for any type of automotive,aviation,marine or industrial purpose.
This technology will provide longer life,lower maintenance and better performance and help produce lower emissions with any turbocharged engine.Red would be a predominate color and the design should communicate the latest technology,economy and
Environmental concern.
This product will initially be distributed in the U.S.A. But should move rapidly to global use.
Updates

Thank you for your design submissions, I have increased the budget for this job because my initial order was too low for the quality of work shown, plus I would Like to see some more options. I have a meeting this Sunday with my other partners and would anticipate being able to give you some feedback by the Beginning of next week. Regards.

Thank you for everyone's participation. The deadline is still open until 6/15 and my partners and I have a meeting Scheduled this weekend. At this time we have not ruled anyone out, But will be making a decision during the course of our meeting and wil Decide which direction we will be going in by the beginning of the week. Thanks again, regards, Dan Ferris.

Hello everybody, Sorry for the delay in communication, we have been very busy in putting the start up together. We are still not decided on the design of the business card and have a wide range to choose from. I would anticipated we shall have an answer within the next two weeks. Regards, Dan Ferris.

Target Market(s)

Manufacturers and wholesalers' of OEM and replacement turbochargers

Industry/Entity Type

Industrial

Contact Information for Business Card

We need a logo that should incorporate the " Nexor, a " possibly super imposed over a turbo charger with the fan blades of the turbocharger showing in the center of the "a" .
Name,title,phone number and email address only, no street/mailing address at this time.
The full name of the company is
" Nexor Turbo Technologies LLC "
For the initial card you can use my info.
Daniel Ferris
VP Sales & Marketing
dferris@nexorturbotechnologies.com
555 014 2876

Requirements
Must have
• The Nexor A, the outline of a turbo charger
Nice to have
• Something classy and simple and worldly (global)
Should not have
• No engines,cars,boats,planes

```html
<!DOCTYPE html>
<html lang="en">
<head>
<meta charset="utf-8">
<title>Nexor Turbo Technologies – Business Card</title>
<link rel="stylesheet" href="https://fonts.googleapis.com/css2?family=Oswald:wght@600&family=Roboto:wght@300;400&display=swap">
<style>
  :root {
    --page-bg: #e9e7e4;
    --card-bg: #f7f6f3;
    --brand-red: #b3121c;
    --band-red: #a8141d;
    --ink: #151515;
    --ink-soft: #3a3a3a;
    --rule: #8a8a8a;
    --icon-bg: #cfcdca;
    --icon-fg: #f7f6f3;
    --band-text: #f3e9e9;
  }
  * { box-sizing: border-box; margin: 0; padding: 0; }
  html, body {
    width: 1200px; height: 1000px; overflow: hidden;
    background: var(--page-bg);
  }
  .card {
    position: absolute; left: 100px; top: 214px;
    width: 1000px; height: 572px;
    background: var(--card-bg);
    box-shadow: 0 6px 24px rgba(0,0,0,.15);
    overflow: hidden;
    font-family: "Roboto", Arial, sans-serif;
  }
  .brand-mark {
    position: absolute; left: 60px; top: 210px;
    display: flex; align-items: center; gap: 18px;
  }
  .brand-mark__dot {
    width: 70px; height: 70px; border-radius: 50%;
    background: var(--brand-red);
  }
  .brand-mark__name {
    font-family: "Oswald", Arial, sans-serif; font-weight: 600;
    font-size: 58px; color: var(--brand-red); letter-spacing: 1px;
  }
  .company-name {
    position: absolute; left: 360px; top: 44px;
    font-family: "Oswald", Arial, sans-serif; font-weight: 600;
    font-size: 46px; color: var(--ink); letter-spacing: .3px;
  }
  .company-rule {
    position: absolute; left: 360px; right: 20px; top: 118px;
    height: 2px; background: var(--rule);
  }
  .contact {
    position: absolute; right: 30px; top: 138px;
    display: flex; flex-direction: column; align-items: flex-end;
  }
  .contact__row {
    display: flex; align-items: center; gap: 14px; height: 58px;
    font-weight: 300; font-size: 34px; color: var(--ink-soft);
  }
  .contact__name { color: var(--brand-red); font-weight: 400; font-size: 42px; }
  .contact__row--name { padding-right: 54px; }
  .icon {
    width: 40px; height: 40px; border-radius: 50%;
    background: var(--icon-bg);
    display: flex; align-items: center; justify-content: center;
  }
  .icon svg { width: 24px; height: 24px; fill: var(--icon-fg); }
  .contact__email {
    position: absolute; right: 60px; top: 366px;
    font-weight: 300; font-size: 34px; color: var(--ink-soft);
  }
  .web-band {
    position: absolute; left: 0; right: 0; top: 430px; height: 142px;
    background: var(--band-red);
  }
  .web-band__url {
    position: absolute; left: 250px; top: 44px;
    font-weight: 300; font-size: 36px; color: var(--band-text);
  }
  .web-band__emblem {
    position: absolute; right: 50px; top: 28px;
    width: 80px; height: 80px; border-radius: 50%;
    background: rgba(255,255,255,.85);
  }
</style>
</head>
<body>
  <div class="card">
    <div class="brand-mark">
      <span class="brand-mark__dot"></span>
      <span class="brand-mark__name">Nexor</span>
    </div>

    <h1 class="company-name">Nexor Turbo Technologies LLC</h1>
    <div class="company-rule"></div>

    <div class="contact">
      <div class="contact__row contact__row--name"><span class="contact__name">Daniel Ferris</span></div>
      <div class="contact__row">
        <span>VP Sales &amp; Marketing</span>
        <span class="icon"><svg viewBox="0 0 24 24"><circle cx="12" cy="8" r="4.5"/><path d="M3 22c0-5 4-8 9-8s9 3 9 8z"/></svg></span>
      </div>
      <div class="contact__row">
        <span>555.014.2876</span>
        <span class="icon"><svg viewBox="0 0 24 24"><path d="M6.6 10.8a15 15 0 0 0 6.6 6.6l2.2-2.2a1 1 0 0 1 1-.25 11.4 11.4 0 0 0 3.6.6 1 1 0 0 1 1 1V20a1 1 0 0 1-1 1A17 17 0 0 1 3 4a1 1 0 0 1 1-1h3.5a1 1 0 0 1 1 1c0 1.25.2 2.45.6 3.6a1 1 0 0 1-.25 1z"/></svg></span>
      </div>
      <div class="contact__row">
        <span style="visibility:hidden">.</span>
        <span class="icon"><svg viewBox="0 0 24 24"><path d="M2 5h20v14H2z" opacity=".0"/><path d="M3 6h18v12H3zM3 6l9 7 9-7" fill="none" stroke="#f7f6f3" stroke-width="2"/></svg></span>
      </div>
    </div>
    <div class="contact__email">dferris@nexorturbotechnologies.com</div>

    <div class="web-band">
      <span class="web-band__url">www.nexorturbotechnologies.com</span>
      <div class="web-band__emblem" role="img" aria-label="Emblem of a globe held in two hands"></div>
    </div>
  </div>
</body>
</html>
```